KAVELUXE Consultancy Business Card

We need a business card design for a new Image & Etiquette Consultancy Company.

The design should reflect the corporate colour found in the logo attached.

Info to include:

Name: Marelda Quon
Title: Image Consultant
Company: KA VELUXE CONSULTANCY
Address: 27 Pelham Street, #14-08 Harbourview Tower, Singapore 048215
Contact: 9317 6408
Email: marelda@kaveluxe.com.sg
Website: www.kaveluxe.com.sg

Industry/Entity Type

Business

```html
<!DOCTYPE html>
<html lang="en">
<head>
<meta charset="utf-8">
<title>KAVELUXE Consultancy – Business Card</title>
<link href="https://fonts.googleapis.com/css2?family=Open+Sans:wght@400;700&display=swap" rel="stylesheet">
<style>
  :root {
    --page-bg: #d9d9d9;
    --purple-deep: #3d1266;
    --purple-mid: #5a2489;
    --purple-light: #7a4ba6;
    --gold: #e8c94a;
    --gold-warm: #f2b93b;
    --band-yellow: #f7c859;
    --band-yellow-light: #fbd878;
    --silver: #d8d8e0;
    --ink-purple: #3f1a6b;
  }
  * { box-sizing: border-box; margin: 0; padding: 0; }
  html, body { width: 1200px; height: 1023px; overflow: hidden; }
  body {
    background: var(--page-bg);
    display: flex;
    flex-direction: column;
    align-items: center;
    justify-content: center;
    gap: 50px;
    font-family: "Open Sans", sans-serif;
  }
  .card {
    position: relative;
    width: 760px;
    height: 456px;
    border-radius: 4px;
    overflow: hidden;
    background:
      radial-gradient(ellipse at 30% 35%, var(--purple-light) 0%, transparent 60%),
      linear-gradient(135deg, var(--purple-mid) 0%, var(--purple-deep) 100%);
    box-shadow: 0 6px 18px rgba(0,0,0,.25);
  }

  /* Brand name placeholder: plain text, one colour, one weight */
  .brand {
    display: flex;
    align-items: center;
    gap: 16px;
    color: var(--gold);
    font-family: "Open Sans", sans-serif;
    font-weight: 400;
    white-space: nowrap;
    line-height: 1;
  }
  .brand-mark {
    flex: none;
    background: var(--gold);
  }

  /* Front */
  .front .brand {
    position: absolute;
    left: 48px;
    top: 110px;
    font-size: 64px;
  }
  .front .brand-mark { width: 40px; height: 40px; }

  .name-band {
    position: absolute;
    left: 0; right: 0;
    top: 262px;
    height: 70px;
    background: linear-gradient(180deg, var(--band-yellow-light), var(--band-yellow));
    border-top: 3px solid var(--silver);
    border-bottom: 3px solid var(--silver);
    display: flex;
    align-items: center;
    justify-content: center;
    gap: 12px;
    color: var(--ink-purple);
  }
  .name-band .person { font-weight: 700; font-size: 20px; letter-spacing: .02em; }
  .name-band .sep { width: 2px; height: 22px; background: var(--ink-purple); }
  .name-band .role { font-size: 15px; }

  .address {
    position: absolute;
    left: 48px;
    top: 354px;
    color: var(--gold-warm);
    font-size: 15px;
    line-height: 1.45;
  }
  .address .company {
    color: var(--gold);
    font-size: 18px;
    letter-spacing: .04em;
    margin-bottom: 4px;
  }
  .contacts {
    position: absolute;
    right: 44px;
    top: 360px;
    list-style: none;
    color: var(--gold-warm);
    font-size: 15px;
    line-height: 1.65;
  }
  .contacts li { display: flex; align-items: center; gap: 9px; }
  .contacts svg { width: 13px; height: 13px; flex: none; }

  /* Back */
  .back .brand {
    position: absolute;
    left: 50%;
    top: 50%;
    transform: translate(-50%, -50%);
    font-size: 84px;
    gap: 20px;
  }
  .back .brand-mark { width: 52px; height: 52px; }
</style>
</head>
<body>

<section class="card front" aria-label="Business card front">
  <div class="brand"><span class="brand-mark" aria-hidden="true"></span>KAVELUXE</div>

  <div class="name-band">
    <span class="person">MARELDA QUON</span>
    <span class="sep"></span>
    <span class="role">Image Consultant</span>
  </div>

  <div class="address">
    <div class="company">KA VELUXE CONSULTANCY</div>
    <div>27 Pelham Street, #14-08 Harbourview Tower,</div>
    <div>Singapore 048215</div>
  </div>

  <ul class="contacts">
    <li>
      <svg viewBox="0 0 13 13" aria-hidden="true"><rect width="13" height="13" rx="2" fill="#f2b93b"/><rect x="4" y="2" width="5" height="9" rx="1" fill="#3d1266"/></svg>
      +65 9317 6408
    </li>
    <li>
      <svg viewBox="0 0 13 13" aria-hidden="true"><rect width="13" height="13" rx="2" fill="#f2b93b"/><rect x="2.5" y="3.5" width="8" height="6" fill="none" stroke="#3d1266" stroke-width="1.2"/><path d="M2.5 3.5 L6.5 7 L10.5 3.5" fill="none" stroke="#3d1266" stroke-width="1.2"/></svg>
      marelda@kaveluxe.com.sg
    </li>
    <li>
      <svg viewBox="0 0 13 13" aria-hidden="true"><rect width="13" height="13" rx="2" fill="#f2b93b"/><circle cx="6.5" cy="6.5" r="4" fill="none" stroke="#3d1266" stroke-width="1.2"/><path d="M2.5 6.5 H10.5 M6.5 2.5 V10.5" stroke="#3d1266" stroke-width="1"/></svg>
      www.kaveluxe.com.sg
    </li>
  </ul>
</section>

<section class="card back" aria-label="Business card back">
  <div class="brand"><span class="brand-mark" aria-hidden="true"></span>KAVELUXE</div>
</section>

</body>
</html>
```